Tiko Marsden Systems Web Site

I need website designed for Tiko Marsden Systems, LLC. It is an email marketing software as a service business. I am looking for a five page website with the ability to accept payments. I have included our logo below for integration with the website. I do not have the text ready yet.

The domain to use is tiko-marsden.example

I have also included some examples of other websites that outline the basic structure I would like
https://trybluvoren.example/
https://www.postquill.example/

I know I need to provide some more information, but I want to get the ball rolling and see what is needed.
Thanks!
Owen

```html
<!DOCTYPE html>
<html lang="en">
<head>
<meta charset="utf-8">
<title>Tiko Marsden Systems – Solution</title>
<link href="https://fonts.googleapis.com/css2?family=Arimo:wght@400;700&family=Oswald:wght@500&display=swap" rel="stylesheet">
<style>
:root{
  --navy:#27265f;
  --navy-deep:#1f1e52;
  --red:#e8202d;
  --ink:#1e2356;
  --text:#555a66;
  --blue:#3f8be0;
  --light-blue:#6fb6f0;
  --card:#f3f3f5;
  --rule:#d9dae0;
  --white:#ffffff;
}
*{margin:0;padding:0;box-sizing:border-box}
html,body{width:1200px;height:2932px;overflow:hidden}
body{position:relative;background:var(--navy);font-family:"Arimo",Arial,sans-serif;color:var(--text)}
.abs{position:absolute}
.backdrop{position:absolute;left:0;top:0}
/* header */
.brand-mark{position:absolute;left:548px;top:10px}
.brand-name{position:absolute;left:0;width:1200px;top:130px;text-align:center;color:var(--light-blue);font-size:24px;letter-spacing:3px}
.nav{position:absolute;left:0;top:184px;width:1200px;height:39px;border-top:1px solid #3a3a7a;border-bottom:1px solid #3a3a7a;display:flex;justify-content:center;align-items:center;gap:40px}
.nav a{color:var(--blue);text-decoration:none;font-variant:small-caps;font-size:15px;font-weight:700;letter-spacing:.5px}
.nav a.current{color:var(--white)}
/* page card */
.page{position:absolute;left:51px;top:238px;width:1098px;height:2374px;background:var(--white)}
.hero{position:absolute;left:84px;top:277px;width:1030px;height:206px;background:linear-gradient(100deg,#2d2a70 0%,#4a4590 40%,#6d6aa8 70%,#3b3880 100%);color:var(--white);text-align:center}
.hero h1{position:absolute;top:42px;width:100%;font-size:25px;font-variant:small-caps;letter-spacing:1px;font-weight:700}
.hero p{position:absolute;top:87px;width:100%;font-size:15px}
.hero .reach{position:absolute;top:144px;left:0;width:100%;display:flex;justify-content:center;align-items:center;gap:40px;font-size:12px;color:var(--light-blue)}
.hero .reach span{display:flex;align-items:center;gap:10px}
.hero .divider{width:1px;height:38px;background:rgba(255,255,255,.5)}
h2{position:absolute;left:131px;font-size:17px;color:var(--ink);font-weight:700}
.lead{position:absolute;left:131px;width:940px;font-size:13px;line-height:19px}
h3{position:absolute;font-size:15px;font-weight:400;color:var(--ink)}
.small{position:absolute;font-size:12px;line-height:16px}
.photo{position:absolute}
.icon-disc{position:absolute;border-radius:50%}
.arrow{display:inline-block;width:0;height:0;border-top:6px solid transparent;border-bottom:6px solid transparent;border-left:8px solid var(--red);margin-right:6px;vertical-align:-1px}
.rule{position:absolute;left:131px;width:940px;height:1px;background:var(--rule)}
.feature{position:absolute;background:var(--card);border:1px solid #e2e3e8}
.feature h4{position:absolute;left:32px;top:30px;font-size:17px;color:var(--ink);line-height:21px}
.feature p{position:absolute;left:32px;width:250px;font-size:13px;line-height:17px}
.feature .shot{position:absolute;right:0;top:0;width:170px;height:100%}
/* footer */
.footer-title{position:absolute;left:117px;top:2660px;font-family:"Oswald",sans-serif;font-size:26px;color:var(--white)}
.address{position:absolute;left:117px;top:2702px;color:var(--white);font-size:13px;line-height:22px}
.address strong{font-size:14px}
.foot-mark{position:absolute;left:604px;top:2662px}
.foot-name{position:absolute;left:529px;width:200px;top:2758px;text-align:center;color:var(--light-blue);font-size:20px;letter-spacing:2px}
.notice{position:absolute;left:788px;top:2668px;width:300px;color:#c9cbe8;font-size:12px;line-height:17px}
.subscribe{position:absolute;left:789px;top:2761px;width:116px;height:30px;border:1px solid var(--light-blue);border-radius:4px;color:var(--light-blue);font-size:13px;display:flex;align-items:center;justify-content:center}
.foot-rule{position:absolute;left:117px;top:2836px;width:966px;height:1px;background:#45458a}
.social{position:absolute;top:2853px;width:40px;height:40px;border:2px solid var(--white);border-radius:50%}
</style>
</head>
<body>

<svg class="backdrop" width="1200" height="2932" aria-hidden="true">
  <polygon points="0,460 1200,290 1200,2550 0,2550" fill="#e8202d"/>
</svg>

<header>
  <svg class="brand-mark" width="104" height="104" aria-hidden="true">
    <circle cx="52" cy="52" r="48" fill="none" stroke="#6fb6f0" stroke-width="3"/>
  </svg>
  <div class="brand-name">TIKO MARSDEN</div>
  <nav class="nav">
    <a href="#">Home</a>
    <a href="#" class="current">Solution</a>
    <a href="#">Pricing</a>
    <a href="#">Customers</a>
    <a href="#">ContactUs</a>
  </nav>
</header>

<main class="page"></main>

<section class="hero" role="img" aria-label="Photo of hands typing on a laptop under a navy tint">
  <h1>Solution</h1>
  <p>Lorem ipsum dolor sit amet, consectetur adipiscing elit. Ut purus ex.</p>
  <div class="reach">
    <span><svg width="22" height="22" viewBox="0 0 24 24" aria-hidden="true"><path d="M6.6 10.8a15 15 0 0 0 6.6 6.6l2.2-2.2a1 1 0 0 1 1-.25 11.4 11.4 0 0 0 3.6.57 1 1 0 0 1 1 1V20a1 1 0 0 1-1 1A17 17 0 0 1 3 4a1 1 0 0 1 1-1h3.5a1 1 0 0 1 1 1c0 1.25.2 2.45.57 3.6a1 1 0 0 1-.25 1z" fill="#fff"/></svg>(555) 014-2276</span>
    <i class="divider"></i>
    <span><svg width="22" height="18" viewBox="0 0 22 18" aria-hidden="true"><rect x="1" y="1" width="20" height="16" rx="2" fill="#fff"/><path d="M1 2l10 8 10-8" fill="none" stroke="#4a4590" stroke-width="1.6"/></svg>Email Us</span>
  </div>
</section>

<h2 style="top:525px">Email List Management</h2>
<p class="lead" style="top:563px">From startups to established companies, keeping a system in place to hold business contacts is critical for sustainable business growth. Sendwise+ offers comprehensive set of functions to create, manage, classify and operate with the email contact lists more effectively.</p>

<h3 style="left:133px;top:646px">Create &amp; Manage</h3>
<div class="photo" style="left:133px;top:680px;width:275px;height:111px;background:linear-gradient(120deg,#5a4a40,#b7a89a 55,#2e2a2a)" role="img" aria-label="Photo of hands working on a laptop keyboard"></div>
<p class="small" style="left:133px;top:805px;width:280px">Create list and list groups to better categorize the list of one sort, perform number of quick actions to manage the list and the contacts within.</p>

<h3 style="left:453px;top:646px">Custom Fields</h3>
<div class="photo" style="left:453px;top:680px;width:275px;height:111px;background:linear-gradient(135deg,#eef0f3,#c9ccd2 60%,#a9aeb7)" role="img" aria-label="Photo of tabbed paper files with coloured index labels"></div>
<p class="small" style="left:453px;top:805px;width:280px">Get rid of storing contacts data in limited number of fields, use custom field function to store additional contact info. Setup as many as you find necessary.</p>

<h3 style="left:774px;top:646px">Suppression List</h3>
<div class="photo" style="left:774px;top:680px;width:275px;height:111px;background:linear-gradient(120deg,#8a5c4a,#d2c1b4 50%,#4d5a55)" role="img" aria-label="Photo of hands using a laptop at a desk"></div>
<p class="small" style="left:774px;top:805px;width:285px">Control how and who do you want to communicate, setup “Don't Send to List” and automatically omit unwanted emails, domains and IPs while sending your campaigns.</p>

<h2 style="top:912px">Cohesive Process of Automation</h2>
<p class="lead" style="top:950px">Sendwise+ offers altogether a new way of workflow automation, creating series of auto follow-ups, creating drip campaigns and setting up event based triggers to automatically take a variety of actions when a contact qualifies for the preset event criteria. Explore the potential of automation to target right audience based on purchase history, behavior and preferences.</p>

<div class="icon-disc" style="left:156px;top:1030px;width:127px;height:127px;background:radial-gradient(circle,#f4f6fa 55%,#dfe4ee)" role="img" aria-label="Illustration of an envelope with a circular arrow"></div>
<h3 style="left:303px;top:1032px">Autoresponder</h3>
<p class="small" style="left:303px;top:1058px;width:290px">Keep recipients interest intact through a sequence of drip campaigns to be delivered automatically. Build and automatically execute the sales workflow that your team can easily follow-up without constant manual work.</p>

<div class="icon-disc" style="left:641px;top:1030px;width:125px;height:125px;background:radial-gradient(circle,#eef3fb 50%,#d7e3f4)" role="img" aria-label="Diagram of icons connected around an event trigger"></div>
<h3 style="left:786px;top:1032px">Event Based Triggers</h3>
<p class="small" style="left:786px;top:1058px;width:285px">Perform a list of actions based on events and give data driven marketing a forward push. Automatically trigger emails when the contacts meet present criteria, celebrate momentous events with contacts and explore several other possibilities with Event Based Triggers.</p>

<h2 style="top:1196px">Smart Segments</h2>
<div class="photo" style="left:131px;top:1237px;width:483px;height:184px;background:radial-gradient(ellipse at 35% 45%,#3d7fd6,#0e2a5c 55%,#04101f)" role="img" aria-label="Photo of a hand reaching toward glowing network icons"></div>
<p class="small" style="left:645px;top:1272px;width:420px;font-size:13px;line-height:18px">Segmentation with all new possibilities to deeply dig your database and create contact groups of similar sort, and segments of contacts with comparable behavior. These better targeted small groups of contacts will help to significantly improve customer engagement and message response rate. Create your next targeted subset using extensive list of filters available at your disposal.</p>

<h2 style="top:1466px">Swift Sending</h2>
<h3 style="left:131px;top:1507px"><i class="arrow"></i>Multithreading</h3>
<p class="small" style="left:131px;top:1530px;width:290px">Accelerate the process of supplying emails to the mail server by setting up system to perform sending activity utilizing parallel connections.</p>
<h3 style="left:455px;top:1507px"><i class="arrow"></i>Multiple Sending Nodes</h3>
<p class="small" style="left:455px;top:1530px;width:290px">With SendwisePlus, a sending node can be connected to variety of couriers and multiple among the connected ones can be selected to send emails from.</p>
<h3 style="left:772px;top:1507px"><i class="arrow"></i>Sending/Masking Domains</h3>
<p class="small" style="left:772px;top:1530px;width:285px">Offers you the extra advantage to not only setup multiple masking domains but also select the ones you prefer for sending email engagement campaigns.</p>

<div class="rule" style="top:1634px"></div>

<h3 style="left:131px;top:1664px"><i class="arrow"></i>Split Testing</h3>
<p class="small" style="left:131px;top:1687px;width:290px">Test different version of campaign in laboratory environment and deliver the best variant of the campaign to ensure maximum conversion rate.</p>
<h3 style="left:455px;top:1664px"><i class="arrow"></i>Flexibility &amp; Customization</h3>
<p class="small" style="left:455px;top:1687px;width:290px">Customize the sending pattern according to your preferences and control sending date and time to leave best possible impact.</p>
<h3 style="left:772px;top:1664px"><i class="arrow"></i>Custom Email Header</h3>
<p class="small" style="left:772px;top:1687px;width:285px">Customize email header of your campaign or SMTP individually for each campaign/SMTP, or even for the groups.</p>

<article class="feature" style="left:129px;top:1813px;width:467px;height:194px">
  <h4>Contact Management</h4>
  <p style="top:62px">Better management of your business contacts illuminates the chances of cross and upsell. Bring in all type of your contacts to store, manage and organize them at one place. Classify and categorize contacts within the lists of your choice.</p>
  <div class="shot" style="background:linear-gradient(160deg,#dfe7f3,#6f8fb8 60%,#2f4d78)" role="img" aria-label="Photo of a finger touching contact icons"></div>
</article>
<article class="feature" style="left:606px;top:1813px;width:467px;height:194px">
  <h4>Campaigns &amp; Reporting</h4>
  <p style="top:62px">Create aesthetically striking HTML campaigns using integrated WSYWYG editor. Schedule to send the campaigns on the desired date &amp; time and to the contacts within the selected list(s), or even to the contacts separated from the list(s) and belongs to a specific Segment.</p>
  <div class="shot" style="background:linear-gradient(160deg,#e8edf4,#a9b7c8 60%,#6c7f97)" role="img" aria-label="Photo of hands over printed report charts"></div>
</article>
<article class="feature" style="left:129px;top:2017px;width:467px;height:303px">
  <h4>Content &amp; Personalization</h4>
  <p style="top:62px">Content remains integral part of email marketing success. As long as it stays relevant for the one whom you are sending it to, the chances of success remain intact. Sendwise+ offers number of options to add dynamic value and fill your content with relevance.</p>
  <div class="shot" style="background:linear-gradient(160deg,#c7d5dc,#7fb8c4 50%,#3e5560)" role="img" aria-label="Photo of hands holding a phone showing content icons"></div>
</article>
<article class="feature" style="left:606px;top:2017px;width:467px;height:303px">
  <h4>Effectively Handle<br>Bounces and Spam</h4>
  <p style="top:82px">High quality email list is essence of whole email marketing; don't let it contaminated with bounces and abuse complaints that pose the biggest threat to your sender reputation. Collect, categorize and process bounced and abuse complaint emails on time with Sendwise+ to avoid the damage.</p>
  <div class="shot" style="background:linear-gradient(160deg,#c9a25c,#5c4a38 55%,#2b2a2a)" role="img" aria-label="Photo of a laptop with floating envelope icons"></div>
</article>

<div class="photo" style="left:260px;top:2374px;width:756px;height:235px;background:radial-gradient(ellipse at 50% 60%,#eef1f7,#ffffff 75%)" role="img" aria-label="Line illustration of a person opening a large envelope surrounded by marketing icons"></div>

<footer>
  <div class="footer-title">Contact</div>
  <div class="address">
    <strong>Tiko Marsden Systems</strong><br>
    207 Harlow Bend Rd.<br>
    Fenwick, OR 97001<br>
    Phone: (555) 014-2276
  </div>
  <svg class="foot-mark" width="52" height="52" aria-hidden="true">
    <circle cx="26" cy="26" r="24" fill="none" stroke="#6fb6f0" stroke-width="2"/>
  </svg>
  <div class="foot-name">TIKO MARSDEN</div>
  <p class="notice">We will soon be launching our new email marketing software as a service (Saas).<br><br>Please stay tuned for important updates.</p>
  <div class="subscribe">Subscribe</div>
  <div class="foot-rule"></div>
  <span class="social" style="left:488px"></span>
  <span class="social" style="left:543px"></span>
  <span class="social" style="left:596px"></span>
  <span class="social" style="left:648px"></span>
</footer>

</body>
</html>
```